Young Balance Support Network

We need a poster explaining that some children live with a disability called Vestibular Disorder. Feel free to ask question. We want you to respect our color code, same as our logo.

Here is our website : http://www.ybsnetwork.org/

We need to sensibilise people about this disability for children.

Industry/Entity Type

Charity

Font styles to use
Serif

Requirements
Must have
• 1. our logo (with all our details) + one of the photo of Marek
• 2. design showing a child with a dizziness for exemple
• 3. a title saying : Aidez-nous à changer la vie des enfants vivant avec un problème vestibulaire
• 4.include the text attached (information flyer YBSN)
• Poster size : 24"X 36"
Should not have
• wheel chair

```html
<!DOCTYPE html>
<html lang="fr">
<head>
<meta charset="utf-8">
<title>Young Balance Support Network – Affiche</title>
<link rel="stylesheet" href="https://fonts.googleapis.com/css2?family=Bodoni+Moda:wght@600;700;800&family=Lora:wght@400;600&display=swap">
<style>
  :root{
    --navy:#12285a;
    --navy-deep:#0d1f48;
    --teal:#2bb3c0;
    --teal-light:#7fd3dc;
    --paper:#ffffff;
    --ink:#3a4356;
    --mist:#eef1f4;
  }
  *{box-sizing:border-box;margin:0;padding:0}
  html,body{width:804px;height:1200px;overflow:hidden;background:var(--paper)}
  .poster{position:relative;width:804px;height:1200px;overflow:hidden;background:var(--paper);font-family:"Lora",Georgia,serif;color:var(--ink)}
  .hero{position:absolute;left:0;top:0;width:804px;height:420px;background:linear-gradient(100deg,#dfe4ea 0%,#f4f6f8 45%,#ffffff 100%)}
  .hero-photo{position:absolute;left:0;top:0;width:430px;height:420px;background:radial-gradient(ellipse at 48% 42%,#e9c6ac 0%,#d7b198 26%,#9bb3c9 48%,#2f3e5c 72%,#d9dee5 100%)}
  .headline{position:absolute;left:430px;top:58px;width:356px;text-align:center;color:var(--navy);font-family:"Bodoni Moda",Georgia,serif;font-weight:700;text-transform:uppercase;line-height:1.08}
  .headline span{display:block;white-space:nowrap}
  .headline .big{font-size:44px}
  .headline .small{font-size:15.5px;margin-top:4px}
  .headline .small + .small{margin-top:2px}
  .headline .big.last{font-size:39px;margin-top:4px}
  .wave{position:absolute;left:0;top:318px;width:804px;height:180px}
  .content{position:absolute;left:0;top:500px;width:804px;height:480px}
  .col{position:absolute;top:0;width:340px}
  .col.left{left:30px}
  .col.right{left:430px}
  .divider{position:absolute;left:402px;top:8px;width:1px;height:440px;background:#d4dbe4}
  .block{margin-bottom:26px}
  .q{display:flex;gap:10px;align-items:flex-start;font-family:"Bodoni Moda",Georgia,serif;font-weight:700;color:var(--navy);font-size:21px;line-height:1.15;text-transform:uppercase;margin-bottom:12px}
  .q svg{flex:0 0 14px;margin-top:5px}
  .a{font-size:10.5px;line-height:1.55;color:var(--ink);padding-left:24px;margin-bottom:8px}
  .brand{position:absolute;left:610px;top:982px;display:flex;align-items:center;gap:10px}
  .brand-dot{width:46px;height:46px;border-radius:50%;background:var(--teal)}
  .brand-name{font-family:"Bodoni Moda",Georgia,serif;font-weight:700;font-size:30px;color:var(--teal)}
  .footer{position:absolute;left:0;top:1040px;width:804px;height:160px}
  .ccp{position:absolute;left:28px;top:1086px;font-family:"Bodoni Moda",Georgia,serif;font-weight:700;font-size:27px;color:var(--paper)}
  .contacts{position:absolute;left:28px;top:1130px;display:grid;grid-template-columns:190px 240px;row-gap:8px;font-size:10.5px;color:var(--paper)}
  .contacts span{display:flex;align-items:center;gap:6px}
  .contacts i{display:inline-block;width:11px;height:11px;border-radius:50%;background:var(--teal)}
  .org{position:absolute;right:28px;top:1140px;text-align:left;width:220px;font-family:"Bodoni Moda",Georgia,serif;font-weight:700;font-size:15px;line-height:1.3;color:var(--paper);text-transform:uppercase}
</style>
</head>
<body>
<main class="poster">
  <section class="hero">
    <div class="hero-photo" role="img" aria-label="Photo de Marek, jeune enfant souriant portant des lunettes bleues"></div>
    <h1 class="headline">
      <span class="big">Aidez-nous</span>
      <span class="small">à changer la vie des</span>
      <span class="small">enfants vivant avec un problème</span>
      <span class="big last">vestibulaire</span>
    </h1>
  </section>

  <svg class="wave" viewBox="0 0 804 180" preserveAspectRatio="none" aria-hidden="true">
    <path d="M0 60 C180 150 420 150 804 20 L804 120 C520 170 260 175 0 150 Z" fill="var(--navy)"/>
    <path d="M0 150 C260 175 520 170 804 120 L804 135 C520 185 260 190 0 168 Z" fill="var(--teal)"/>
    <path d="M0 168 C260 190 520 185 804 135 L804 180 L0 180 Z" fill="var(--paper)"/>
  </svg>

  <section class="content">
    <div class="divider"></div>
    <div class="col left">
      <div class="block">
        <h2 class="q"><svg width="14" height="18" viewBox="0 0 14 18"><path d="M2 2 L11 9 L2 16" fill="none" stroke="var(--teal)" stroke-width="3"/></svg>Qu'est-ce que le vestibule ?</h2>
        <p class="a">C'est un organe sensoriel, pilier de votre équilibre, véritable GPS situé dans l'oreille interne.</p>
      </div>
      <div class="block">
        <h2 class="q"><svg width="14" height="18" viewBox="0 0 14 18"><path d="M2 2 L11 9 L2 16" fill="none" stroke="var(--teal)" stroke-width="3"/></svg>Quelles en sont les conséquences pour l'enfant ?</h2>
        <p class="a">Le développement moteur de l'enfant est retardé car il doit trouver des solutions afin de construire son équilibre, stabiliser son regard et son corps.</p>
        <p class="a">Certains apprentissages sont de véritables obstacles pour l'enfant : se représenter son propre corps, se situer dans l'espace, s'orienter, marcher, lire, écrire. Chacun de ces actes demande des efforts considérables et une grande fatigue.</p>
        <p class="a">Quand l'enfant réussit à effectuer l'une de ces actions, son comportement peut sembler étrange et bien trop souvent mal interprété par le grand public.</p>
      </div>
    </div>
    <div class="col right">
      <div class="block">
        <h2 class="q"><svg width="14" height="18" viewBox="0 0 14 18"><path d="M2 2 L11 9 L2 16" fill="none" stroke="var(--teal)" stroke-width="3"/></svg>Qu'est-ce qu'une aréflexie vestibulaire ?</h2>
        <p class="a">C'est l'absence complète de toute information vestibulaire. L'enfant a alors l'impression que tout vacille autour de lui, jour et nuit.</p>
      </div>
      <div class="block">
        <h2 class="q"><svg width="14" height="18" viewBox="0 0 14 18"><path d="M2 2 L11 9 L2 16" fill="none" stroke="var(--teal)" stroke-width="3"/></svg>Quel est le but de notre association ?</h2>
        <p class="a">Notre association a pour but de promouvoir les troubles vestibulaires chez l'enfant, ses conséquences sur sa santé ainsi que celle de son entourage et de soutenir les enfants et leurs parents en leur offrant un espace de parole et des solutions concrètes pour soulager leur quotidien.</p>
        <p class="a">Notre association a également pour but de financer et promouvoir toute action de recherche scientifique visant à aider les enfants ayant un trouble vestibulaire.</p>
      </div>
    </div>
  </section>

  <div class="brand">
    <span class="brand-dot"></span>
    <span class="brand-name">YBSN</span>
  </div>

  <svg class="footer" viewBox="0 0 804 160" preserveAspectRatio="none" aria-hidden="true">
    <path d="M0 30 C220 10 480 40 804 80 L804 160 L0 160 Z" fill="var(--teal)"/>
    <path d="M0 40 C220 22 480 52 804 92 L804 160 L0 160 Z" fill="var(--navy)"/>
  </svg>

  <div class="ccp">CCP: 12-345678-9</div>
  <div class="contacts">
    <span><i></i>www.ybsnetwork.org</span>
    <span><i></i>/YoungBalanceSupportNetwork</span>
    <span><i></i>info@ybsnetwork.org</span>
    <span><i></i>@YBSNetwork</span>
  </div>
  <div class="org">Young Balance<br>Support Network</div>
</main>
</body>
</html>
```